Real Estate Biz Card

-Card Size: Standard
-Background: Dark grey or black. I am open to gradient or a textured background.
-Other Colors: I dont mind pops of color. Contrasty blue, lime green, red Etc. Feel free to get creative.
-Text color: be creative
-Font: I like modern styles. Something that works well with my KV718 logo. See attached
-I would like my logo (KV718) watermarked on the card. Either on one side or both.
-Front of Card: keep it simple. Head shot, name, Logo, Phone #
-Back: add the rest of the details. See list below.
-brokerages logo as well as the Dwellon and Equal Housing Opportunity logos on the card
-Name: Milo Dravek
-Residential Real Estate
-Cell:
-Email:
-Site:
-Office Address:
-very small/fine print "Each office independently owned & operated

```html
<!DOCTYPE html>
<html lang="en">
<head>
<meta charset="utf-8">
<title>KV718 Business Card</title>
<link href="https://fonts.googleapis.com/css2?family=Montserrat:wght@500;600&family=Open+Sans:wght@400;600;700&display=swap" rel="stylesheet">
<style>
  :root {
    --stage: #2b2b2d;
    --card-black: #1c1d20;
    --card-blue: #1a78c8;
    --card-grey: #8b8b8d;
    --strip-grey: #7d7d80;
    --ink-dark: #26272a;
    --white: #ffffff;
    --photo-top: #c9cbce;
    --photo-bottom: #7f8fa8;
  }
  * { box-sizing: border-box; margin: 0; padding: 0; }
  html, body { width: 1200px; height: 900px; overflow: hidden; }
  body {
    background: var(--stage);
    font-family: "Open Sans", Arial, sans-serif;
    display: flex;
    flex-direction: column;
    align-items: center;
    justify-content: center;
    gap: 36px;
  }
  .card {
    position: relative;
    width: 700px;
    height: 400px;
    overflow: hidden;
    box-shadow: 0 10px 26px rgba(0,0,0,.45);
  }

  /* Back side */
  .card-back { background: var(--card-grey); }
  .back-mark {
    position: absolute;
    left: 0; right: 0; top: 110px;
    text-align: center;
    font-family: "Montserrat", Arial, sans-serif;
    font-weight: 600;
    font-size: 96px;
    letter-spacing: 6px;
    color: var(--ink-dark);
  }
  .back-badges {
    position: absolute;
    left: 0; right: 0; bottom: 60px;
    display: flex;
    justify-content: center;
    align-items: center;
    gap: 12px;
  }
  .badge { width: 22px; height: 22px; background: var(--ink-dark); }
  .brokerage {
    font-family: "Open Sans", Arial, sans-serif;
    font-weight: 600;
    font-size: 15px;
    letter-spacing: 1px;
    color: var(--ink-dark);
    margin-left: 6px;
  }

  /* Front side */
  .card-front { background: var(--card-blue); }
  .front-dark {
    position: absolute; inset: 0;
    background: var(--card-black);
    clip-path: polygon(0 0, 100% 0, 100% 42%, 62% 42%, 62% 60%, 0 60%);
  }
  .fine-print-strip {
    position: absolute; left: 0; right: 0; bottom: 0;
    height: 36px;
    background: var(--strip-grey);
    color: var(--white);
    font-size: 13px;
    line-height: 36px;
    padding-left: 34px;
  }
  .logo-name {
    position: absolute;
    left: 34px; top: 140px;
    font-family: "Montserrat", Arial, sans-serif;
    font-weight: 600;
    font-size: 74px;
    letter-spacing: 3px;
    color: var(--card-blue);
    line-height: 1;
  }
  .headshot {
    position: absolute;
    left: 470px; top: 36px;
    width: 200px; height: 190px;
    border-radius: 16px;
    background: linear-gradient(180deg, var(--photo-top) 0%, var(--photo-top) 45%, var(--photo-bottom) 100%);
    border: 2px solid #1a4f82;
  }
  .agent {
    position: absolute;
    right: 30px; top: 240px;
    text-align: right;
    color: var(--white);
  }
  .agent-name { font-weight: 700; font-size: 18px; letter-spacing: .5px; }
  .agent-role { font-size: 17px; margin-top: 2px; }
  .contact {
    position: absolute;
    left: 34px; top: 250px;
    color: var(--white);
    font-size: 15px;
    line-height: 18px;
    list-style: none;
  }
  .contact li { display: flex; align-items: center; gap: 8px; }
  .contact svg { width: 14px; height: 14px; fill: var(--white); flex: none; }
</style>
</head>
<body>

<section class="card card-back" aria-label="Card back">
  <div class="back-mark">KV718</div>
  <div class="back-badges">
    <span class="badge" aria-label="Dwellon membership badge"></span>
    <span class="badge" aria-label="Equal housing badge"></span>
    <span class="brokerage">NORTHGATE REALTY</span>
  </div>
</section>

<section class="card card-front" aria-label="Card front">
  <div class="front-dark"></div>
  <div class="headshot" role="img" aria-label="Agent head shot"></div>
  <div class="logo-name">KV718</div>
  <div class="agent">
    <div class="agent-name">MILO DRAVEK</div>
    <div class="agent-role">Residential Real Estate</div>
  </div>
  <ul class="contact">
    <li>1420 Alder Court</li>
    <li>Juneau, Alaska 99801</li>
    <li><svg viewBox="0 0 16 16"><path d="M3 1h3l1 4-2 1c1 2 3 4 5 5l1-2 4 1v3c0 1-1 2-2 2C7 15 1 9 1 3c0-1 1-2 2-2z"/></svg>555 210 4471</li>
    <li><svg viewBox="0 0 16 16"><path d="M4 0h8a1 1 0 0 1 1 1v14a1 1 0 0 1-1 1H4a1 1 0 0 1-1-1V1a1 1 0 0 1 1-1zm1 2v10h6V2zm3 11a1 1 0 1 0 0 2 1 1 0 0 0 0-2z"/></svg>555 382 1906</li>
    <li><svg viewBox="0 0 16 16"><path d="M0 3h16v10H0zm1.5 1.2V5l6.5 4.2L14.5 5v-.8L8 8.3z"/></svg>milo@kv718.com</li>
    <li><svg viewBox="0 0 16 16"><path d="M8 0a8 8 0 1 0 0 16A8 8 0 0 0 8 0zm0 2a6 6 0 0 1 0 12c2-2 2-10 0-12zm-1 .1C5 4 5 12 7 13.9A6 6 0 0 1 7 2.1z"/></svg>www.kv718.com</li>
  </ul>
  <div class="fine-print-strip">Each office independently owned &amp; operated</div>
</section>

</body>
</html>
```